Cutting Edge Property Services Provider is Looking to Update Business Card Design

We are looking to freshen up our business cards to match our cutting edge technology based image.

QUARVO-LYN - Where Service Meets Technology

More information about our company can be found on our website at www.quarvo-lyn.example

We integrate technology in a historically low tech industry.

We have appeared on the Brisk 300/3000 list 2 years in a row and we're previously recognized as the 5th Fastest Growing Company in San Diego.

Our core colors are blue and white, but are not against accents that might improve our image.

We currently have our Mission Statement on our Business Cards in a folding design:
QUARVO-LYN IS THE LEADING BUILDING SERVICES INNOVATOR. BY COMBINING TECHNOLOGY WITH FUNCTIONAL TOOS THAT IMPROVE EFFICIENCY IN THE WORKPLACE, WE PROVIDE UNPARALLELED SERVICE IN THE INDUSTRY. DEVELOPING LASTING RELATIONSHIPS WITH OUR CLIENTS AND ASSOCIATES IS THE CORNERSTONE OF OUR SUCCESS.

We'd like to convey the image of a cutting edge, technology based company. Want the cards to pop.

Target Market(s)

Commercial Property Managers - 20 to 50 year old professionals

Industry/Entity Type

Business

Requirements
Must have
• Must utilize our logo obviously, but are definitely open to using variations on the logo. Utilizing the components of the logo, but maybe in different configurations or backgrounds, etc...

Must use the Name: QUARVO-LYN.
Can also use QUARVO-LYN PROPERTY SERVICES.

Must include the Mission Statement

Must say: Where Service Meets Technology
Nice to have
• We are considering plastic stock, shaped cards, or folding cards.

Nothing over the top or really expensive, but will consider if it conveys innovation and technology.
Should not have
• No images of toilets, buildings, trees, or anything relating to commercial properties.

We want to convey our technology image.

```html
<!DOCTYPE html>
<html lang="en">
<head>
<meta charset="utf-8">
<title>QUARVO-LYN Folding Business Card</title>
<link rel="stylesheet" href="https://fonts.googleapis.com/css2?family=PT+Sans:wght@400;700&family=Ubuntu:wght@700&display=swap">
<style>
  :root {
    --brand-blue: #0b4a7d;
    --brand-blue-soft: #1d5d8f;
    --label-red: #e3231f;
    --card-white: #ffffff;
    --pattern-tint: #dfe6ee;
    --board-dark: #1b1b1b;
    --board-mid: #2c2c2c;
    --ink-dark: #222831;
  }
  * { margin: 0; padding: 0; box-sizing: border-box; }
  html, body { width: 1200px; height: 810px; overflow: hidden; }
  body {
    position: relative;
    background: repeating-linear-gradient(90deg, var(--board-dark) 0 3px, var(--board-mid) 3px 5px, #202020 5px 9px);
    font-family: "PT Sans", sans-serif;
  }
  .panel-label {
    position: absolute;
    width: 543px;
    text-align: center;
    font-family: "Ubuntu", sans-serif;
    font-weight: 700;
    font-size: 35px;
    letter-spacing: 5px;
    color: var(--label-red);
  }
  .label-inner-top { left: 52px; top: 20px; }
  .label-front { left: 623px; top: 20px; }
  .label-inner-bottom { left: 52px; top: 728px; }
  .label-back { left: 623px; top: 728px; }

  .card {
    position: absolute;
    width: 543px;
    height: 308px;
    background: var(--card-white);
    border-radius: 26px;
    overflow: hidden;
  }
  .card-inner-top { left: 52px; top: 80px; }
  .card-front { left: 623px; top: 80px; }
  .card-inner-bottom { left: 52px; top: 408px; }
  .card-back { left: 623px; top: 408px; }

  .brand-name {
    font-family: "PT Sans", sans-serif;
    font-weight: 700;
    color: var(--brand-blue);
    letter-spacing: 2px;
    white-space: nowrap;
  }

  /* Inner top */
  .card-inner-top .brand-mark {
    position: absolute; left: 0; right: 0; top: 108px;
    display: flex; justify-content: center; align-items: center; gap: 16px;
  }
  .card-inner-top .brand-square {
    width: 44px; height: 44px; border-radius: 8px; background: var(--brand-blue);
  }
  .card-inner-top .brand-name { font-size: 52px; }
  .card-inner-top .web-address {
    position: absolute; left: 0; right: 0; top: 264px;
    text-align: center; font-size: 20px; letter-spacing: 3px; color: var(--ink-dark);
  }

  /* Front */
  .card-front .brand-mark {
    position: absolute; left: 36px; top: 42px;
    display: flex; align-items: center; gap: 12px;
  }
  .card-front .brand-square {
    width: 30px; height: 30px; border-radius: 6px; background: var(--brand-blue);
  }
  .card-front .brand-name { font-size: 34px; }
  .contact-list {
    position: absolute; left: 36px; top: 186px; list-style: none;
    font-size: 14.5px; color: var(--ink-dark);
  }
  .contact-list li { display: flex; align-items: center; gap: 7px; height: 24px; }
  .contact-list svg { width: 12px; height: 12px; flex: none; }
  .contact-list .web { letter-spacing: 1.5px; }
  .person {
    position: absolute; right: 46px; top: 206px; text-align: right;
  }
  .person-name { font-size: 21px; font-weight: 700; letter-spacing: 1.5px; color: var(--brand-blue); line-height: 1; }
  .person-title { font-size: 13px; font-weight: 700; color: var(--ink-dark); margin-top: 3px; letter-spacing: .5px; }
  .address-band {
    position: absolute; left: 0; right: 0; bottom: 0; height: 32px;
    background: var(--brand-blue); color: var(--card-white);
    font-size: 14.5px; padding-left: 36px; line-height: 32px;
  }

  /* Inner bottom */
  .faint-backdrop {
    position: absolute; inset: 0;
    background: radial-gradient(ellipse 60% 55% at 50% 55%, var(--pattern-tint) 0%, rgba(223,230,238,.45) 55%, rgba(255,255,255,0) 100%);
  }
  .mission {
    position: absolute; left: 30px; right: 30px; top: 64px;
    text-align: center; font-size: 16px; line-height: 30px; color: var(--brand-blue-soft);
  }

  /* Back */
  .pattern-backdrop {
    position: absolute; inset: 0;
    background: linear-gradient(180deg, #e9eef3 0%, var(--pattern-tint) 50%, #e9eef3 100%);
  }
  .card-back .brand-name {
    position: absolute; left: 0; right: 0; top: 110px;
    text-align: center; font-size: 60px; letter-spacing: 3px;
  }
  .tagline {
    position: absolute; left: 0; right: 0; top: 244px;
    text-align: center; font-size: 25px; font-weight: 700; color: var(--brand-blue);
  }
</style>
</head>
<body>
  <div class="panel-label label-inner-top">Inner Top</div>
  <div class="panel-label label-front">Front</div>
  <div class="panel-label label-inner-bottom">Inner Bottom</div>
  <div class="panel-label label-back">Back</div>

  <section class="card card-inner-top">
    <div class="brand-mark">
      <span class="brand-square"></span>
      <span class="brand-name">QUARVO-LYN</span>
    </div>
    <p class="web-address">www.quarvo-lyn.example</p>
  </section>

  <section class="card card-front">
    <div class="brand-mark">
      <span class="brand-square"></span>
      <span class="brand-name">QUARVO-LYN</span>
    </div>
    <ul class="contact-list">
      <li>
        <svg viewBox="0 0 12 12"><path d="M3 1 L5 3.5 L4 5 Q5 7 7 8 L8.5 7 L11 9 L9.5 11 Q4 10.5 1 3 Z" fill="var(--ink-dark)"/></svg>
        1 (800) 555-0142
      </li>
      <li>
        <svg viewBox="0 0 12 12"><rect x="1" y="3" width="10" height="7" fill="none" stroke="var(--ink-dark)" stroke-width="1.4"/><path d="M1 3 L6 7 L11 3" fill="none" stroke="var(--ink-dark)" stroke-width="1.2"/></svg>
        info@quarvo-lyn.example
      </li>
      <li class="web">
        <svg viewBox="0 0 12 12"><circle cx="6" cy="6" r="5" fill="none" stroke="var(--ink-dark)" stroke-width="1.2"/><ellipse cx="6" cy="6" rx="2.2" ry="5" fill="none" stroke="var(--ink-dark)" stroke-width="1"/><path d="M1 6 H11" stroke="var(--ink-dark)" stroke-width="1"/></svg>
        www.quarvo-lyn.example
      </li>
    </ul>
    <div class="person">
      <p class="person-name">Your Name</p>
      <p class="person-title">Title</p>
    </div>
    <div class="address-band">1250 Harbor Crest Blvd., Suite 200, San Diego, CA 92101</div>
  </section>

  <section class="card card-inner-bottom">
    <div class="faint-backdrop" role="img" aria-label="Faint large brand symbol watermark behind the mission statement"></div>
    <p class="mission">QUARVO-LYN is The Leading Building Services Innovator.<br>By Combining Technology With Functional Toos That<br>Improve Efficiency In The Workplace, We Provide<br>Unparalleled Service in The Industry. Developing<br>Lasting Relationships With Our Clients and Associates<br>is The Cornerstone of Our Success.</p>
  </section>

  <section class="card card-back">
    <div class="pattern-backdrop" role="img" aria-label="Repeating pale pattern of the brand symbol covering the card"></div>
    <p class="brand-name">QUARVO-LYN</p>
    <p class="tagline">Where Service Meets Technology</p>
  </section>
</body>
</html>
```